image or html template for an Email Sales Campaign – offer for a One-off Press Release

We need a design for an email promotion we are sending to existing and potential clients. We are an international digital PR platform service called Quill Harbour. See www.quillharbour-demo.com

With this email promotion we would like to push our "Single Dispatch" service. With this service a client can purchase the ability to send a press release to our database of 4800 journalists. These journalists registered to our site are from publications such as Vantor, Hearth Weekly, Evening Ledger Trend, Plum Journal, Mira Interiors, Morning Post, VX, Zest! Journal and many others. We will be offering a special price for the service, £30 instead of £45. It will be a one off fee, with no further commitment.

With this release the client will be able to:
-upload up to 8 images to accompany their release
-personalise the release by adding their companies logo
-add caption information and stockist details to each image so that journalists have everything they need to feature their products
-email it directly to journalist's inbox's
-add their own list of contacts to be emailed too
-their press release will also be added to our release page for journalists to access 24/7

See more on information on the service here: http://www.quillharbour-demo.com/services/clients/dispatchbay.php?tid=1

The image we would like designed to send out as part of an email needs to take up around 1/3 of the space of a typical email. It needs to be clean and simple but fun, modern and eye catching. With graphics that are engaging but fit with our site's aesthetic. We can use images from the site (clients products) if this works. There is a deadline for the offer. This doesn't have to be HTML just a good "image", which contains products/banners/information etc, we can put in as the main part of the email

Email marketing we have previously sent:
http://clipvault-demo.com/t/qp41Rz7k
http://clipvault-demo.com/t/8m2wKod9hTzu
http://clipvault-demo.com/t/rbVQut5w

Email marketing we like:
http://clipvault-demo.com/t/nXwPe2k8Hd
http://clipvault-demo.com/t/KfTyab47zR
http://clipvault-demo.com/t/MeqtRnoP
http://clipvault-demo.com/t/7kzzgfaMJ2

Target Market(s)

Interiors and Gifts companies/online retailers

Industry/Entity Type

Marketing

Requirements
Must have
• Must be modern and fun
Must convey or complement some of the key elements of the service being offered
Must be bright
Must show the offered price or highlight the discount/saving

```html
<!DOCTYPE html>
<html lang="en">
<head>
<meta charset="utf-8">
<title>Quill Harbour – Single Dispatch offer</title>
<link rel="stylesheet" href="https://fonts.googleapis.com/css2?family=Alice&family=Archivo+Narrow:wght@400;700&family=Libre+Franklin:wght@400;500&display=swap">
<style>
  :root {
    --stage: #333333;
    --paper: #ffffff;
    --brand-red: #9e1b32;
    --deep-red: #4e0c17;
    --slate: #4a4a4a;
    --grey-text: #8a8a8a;
    --icon-grey: #a3a3a3;
    --logo-grey: #6f6f6f;
    --rule: #b8b8b8;
  }
  * { margin: 0; padding: 0; box-sizing: border-box; }
  html, body { width: 1154px; height: 1200px; overflow: hidden; background: var(--stage); }
  body { position: relative; font-family: "Libre Franklin", Arial, sans-serif; }

  .email { position: absolute; left: 50px; top: 34px; width: 1055px; height: 1130px; background: var(--paper); }
  .abs { position: absolute; }

  .brand-name { left: 266px; top: 26px; font-size: 30px; font-weight: 400; color: var(--logo-grey); letter-spacing: 0.5px; }

  .social { display: flex; gap: 8px; }
  .social span { width: 32px; height: 32px; border-radius: 50%; background: var(--icon-grey); display: block; }
  .social--header { left: 628px; top: 34px; }

  .band-red { left: 0; top: 118px; width: 100%; height: 42px; background: var(--brand-red); }
  .band-slate { left: 0; top: 160px; width: 100%; height: 36px; background: var(--slate); }

  .hero-headline { left: 298px; top: 290px; font-family: "Alice", Georgia, serif; font-weight: 400; font-size: 54px; line-height: 60px; color: var(--brand-red); }
  .hero-photo { left: 548px; top: 214px; width: 476px; height: 268px; background: radial-gradient(ellipse at 55% 55%, #eee7da 0%, #d8c9aa 38%, #f4f1ec 70%, #ffffff 100%); }

  .offer-band { left: 0; top: 538px; width: 100%; height: 53px; background: var(--brand-red); color: #fff; font-size: 22px; text-align: center; line-height: 53px; }
  .offer-band strong { font-size: 26px; font-weight: 500; }

  .dotted-rule { left: 260px; top: 602px; width: 538px; border-top: 1px dashed var(--rule); }

  .product { top: 619px; width: 148px; height: 389px; background: var(--brand-red); border: 1px solid #d7d7d7; }
  .product--one { left: 275px; }
  .product--two { left: 448px; }
  .product--three { left: 628px; }
  .product__photo { height: 118px; }
  .product--one .product__photo { background: linear-gradient(180deg, #dcdcd8, #c9c9c4); }
  .product--two .product__photo { background: linear-gradient(180deg, #d9d1c4, #b9ab98 70%, #8f8374); }
  .product--three .product__photo { background: linear-gradient(180deg, #ffffff, #ece4d3 60%, #f7f5f0); }
  .product__title { height: 31px; line-height: 31px; text-align: center; color: #fff; font-family: "Archivo Narrow", "Arial Narrow", sans-serif; font-weight: 700; font-size: 16px; }
  .product__price { height: 27px; line-height: 27px; text-align: center; color: #fff; background: var(--deep-red); font-family: "Archivo Narrow", "Arial Narrow", sans-serif; font-weight: 700; font-size: 16px; }
  .product__text { padding: 2px 4px 0 3px; color: #fff; font-size: 12.4px; line-height: 20px; }
  .product__button { position: absolute; left: 19px; bottom: 12px; width: 110px; height: 23px; border-radius: 12px; border: 1px solid #cfcfcf; background: linear-gradient(180deg, #6a6a6a, #2f2f2f); color: #fff; font-size: 12px; text-align: center; line-height: 21px; }

  .footer { left: 0; top: 1044px; width: 100%; height: 86px; background: var(--slate); }
  .footer__url { left: 274px; top: 6px; color: #fff; font-size: 18px; }
  .footer__contact { left: 276px; top: 32px; color: #fff; font-size: 11.5px; display: flex; align-items: center; gap: 5px; }
  .footer__contact svg { display: block; }
  .footer__legal { left: 274px; top: 50px; color: var(--grey-text); font-size: 11.5px; }
  .social--footer { left: 628px; top: 21px; }
</style>
</head>
<body>
  <main class="email">
    <header>
      <div class="abs brand-name">Quill Harbour</div>
      <nav class="abs social social--header" aria-label="Social links"><span></span><span></span><span></span><span></span></nav>
    </header>
    <div class="abs band-red"></div>
    <div class="abs band-slate"></div>

    <section>
      <h1 class="abs hero-headline">Your PR<br>for only<br>£30</h1>
      <div class="abs hero-photo" role="img" aria-label="Cream upholstered chaise longue with an ornate gilded frame"></div>
    </section>

    <div class="abs offer-band"><strong>£30</strong> Single Dispatch instead of £45 – Offer Ends 30 June</div>
    <div class="abs dotted-rule"></div>

    <article class="abs product product--one">
      <div class="product__photo" role="img" aria-label="Red swivel armchair against a concrete wall"></div>
      <h2 class="product__title">Single Dispatch</h2>
      <div class="product__price">£30 instead of £45</div>
      <p class="product__text">Send one press release to our 4800 journalists from Vantor, Hearth Weekly, VX and more. A one off fee, with no further commitment.</p>
      <div class="product__button">Know More</div>
    </article>
    <article class="abs product product--two">
      <div class="product__photo" role="img" aria-label="White sofa with colourful cushions in a living room"></div>
      <h2 class="product__title">Your Own Logo</h2>
      <div class="product__price">Up to 8 Images</div>
      <p class="product__text">Upload up to 8 images with your company logo. Add captions and stockist details so journalists have all they need to feature you.</p>
      <div class="product__button">Know More</div>
    </article>
    <article class="abs product product--three">
      <div class="product__photo" role="img" aria-label="Ornate gilded chaise longue in cream upholstery"></div>
      <h2 class="product__title">Direct to Inbox</h2>
      <div class="product__price">Online 24/7</div>
      <p class="product__text">Email it straight to journalists' inboxes, add your own list of contacts, and your release stays on our release page 24/7.</p>
      <div class="product__button">Know More</div>
    </article>

    <footer class="abs footer">
      <div class="abs footer__url">www.quillharbour-demo.com.au</div>
      <div class="abs footer__contact">
        <svg width="12" height="9" viewBox="0 0 12 9" aria-hidden="true"><rect x="0.5" y="0.5" width="11" height="8" fill="#fff" stroke="#c23a4e"/><path d="M0.5 0.5 L6 5 L11.5 0.5" fill="none" stroke="#c23a4e"/></svg>
        <span>info@quillharbour-demo.com.au</span>
        <svg width="10" height="11" viewBox="0 0 10 11" aria-hidden="true" style="margin-left:4px"><path d="M2 0.5 L4 3 L3 4.5 Q4.5 7 6.5 8 L8 7 L9.5 9 L8 10.5 Q3 10 0.5 2 Z" fill="#c23a4e"/></svg>
        <span>02 90000417</span>
      </div>
      <div class="abs footer__legal">©2013 Quill Harbour all Right Reserved &nbsp;- Terms &amp; Privacy</div>
      <nav class="abs social social--footer" aria-label="Social links"><span></span><span></span><span></span><span></span></nav>
    </footer>
  </main>
</body>
</html>
```